REDESIGN COUPLE PAGES FOR SURGE VIDEO ADS

PLEASE REDESIGN THIS PAGE FOR ME:
http://pagekitfinder.com/rk/milo/surge/pricing.html
I need it to be easy to read for the end user so the customer knows exactly what he will be getting. Make an emphasis on the subscription as the most popular item....and also the price per video format should be emphasized too.

Target Market(s)

B2B

Industry/Entity Type

Video Production

Number of Pages Required

3 page

Colors

Designer to choose colors to be used in the design.

Requirements
Must have
• PLEASE REDESIGN THIS PAGE FOR ME:
• http://pagekitfinder.com/rk/milo/surge/pricing.html
• I need it to be easy to read for the end user so the customer knows exactly what he will be getting. Make an emphasis on the subscription as the most popular item....and also the price per video format should be emphasized too.
Nice to have
Should not have

```html
<!DOCTYPE html>
<html lang="en">
<head>
<meta charset="utf-8">
<title>SURGE – Pricing</title>
<link href="https://fonts.googleapis.com/css2?family=Lato:wght@400;700;900&display=swap" rel="stylesheet">
<style>
:root{
  --navy:#161d2e;
  --navy-2:#1c2438;
  --blue:#3b6fe0;
  --blue-light:#5f8ef0;
  --sky:#bcd3f5;
  --accent:#e4572e;
  --line:#c9ccd3;
  --text:#1a1a1a;
  --white:#ffffff;
  --muted:#dfe3ea;
}
*{margin:0;padding:0;box-sizing:border-box}
html,body{width:776px;height:1200px;overflow:hidden}
body{font-family:'Lato',sans-serif;background:var(--white);color:var(--text);position:relative}

.site-header{position:absolute;left:0;top:0;width:776px;height:62px;background:var(--navy)}
.brand{position:absolute;left:85px;top:18px;color:var(--muted)}
.brand-name{display:flex;align-items:center;gap:4px;font-weight:900;font-size:19px;letter-spacing:3px;line-height:1}
.brand-mark{width:12px;height:12px;background:var(--blue-light)}
.brand-tag{font-size:5.6px;letter-spacing:1px;margin-top:4px;font-weight:700}
.main-nav{position:absolute;left:254px;top:24px;display:flex;gap:9px;font-size:9.3px;color:var(--white)}
.main-nav .active{color:var(--blue-light)}
.login{position:absolute;left:607px;top:24px;font-size:9.3px;color:var(--white)}
.signup{position:absolute;left:639px;top:18px;width:52px;height:26px;border-radius:2px;background:linear-gradient(180deg,var(--blue-light),var(--blue));color:var(--white);font-size:9.3px;display:flex;align-items:center;justify-content:center}

.page-title{position:absolute;left:0;top:92px;width:776px;text-align:center;font-weight:900;font-size:16px;letter-spacing:-.2px}

.pricing{position:absolute;left:85px;top:140px;width:605px;height:783px;display:flex}
.col{width:101px;position:relative;border-left:1px solid var(--line)}
.col:last-child{border-right:1px solid var(--line)}
.col-head{height:101px;background:var(--navy);color:var(--white);text-align:center;border-bottom:2px solid var(--accent)}
.plan-name{height:51px;padding-top:9px;border-bottom:1px solid #2b3450}
.plan-name h2{font-size:10.5px;font-weight:900;letter-spacing:-.2px}
.plan-name p{font-size:6.6px;font-weight:900;line-height:7px;margin-top:4px;padding:0 4px}
.plan-price{height:48px;padding-top:7px;font-size:7.2px}
.plan-price strong{display:block;font-size:12.5px;font-weight:900;line-height:14px}
.features-head{display:flex;align-items:center;justify-content:center;font-size:12px;font-weight:900}
.col.popular{box-shadow:0 0 10px rgba(0,0,0,.18);z-index:2}
.col.popular .plan-name{background:linear-gradient(180deg,var(--blue-light),var(--blue));border-bottom:0}
.col.popular .plan-price{background:var(--sky);color:var(--text)}
.cells{padding-top:2px}
.cell{height:25.85px;margin:0 7px;border-bottom:1px solid var(--line);display:flex;align-items:center;font-size:5.6px;padding-left:1px;line-height:6px}
.qty{height:26px;display:flex;align-items:center;justify-content:center;margin:0 7px;border-bottom:1px solid var(--line)}
.qty span{width:9px;height:9px;border:1px solid #9aa6bf;font-size:5.6px;display:flex;align-items:center;justify-content:center;background:#eef2f8}
.sum{height:25.85px;margin:0 7px;border-bottom:1px solid var(--line);display:flex;justify-content:space-between;align-items:center;font-size:6px;padding:0 4px 0 2px}
.sum.grand{font-weight:700}
.buy{display:inline-flex;align-items:center;justify-content:center;width:52px;height:18px;border-radius:2px;background:linear-gradient(180deg,var(--blue),var(--blue-light));color:var(--white);font-size:6px;font-weight:900;margin:7px 0 0 7px}
.buy.low{margin-top:10px}

.site-footer{position:absolute;left:0;top:993px;width:776px;height:207px;background:var(--navy);color:var(--white)}
.footer-brand{position:absolute;left:85px;top:38px;color:var(--muted)}
.footer-brand .brand-name{font-size:25px;letter-spacing:4px}
.footer-brand .brand-mark{width:15px;height:15px}
.footer-brand .brand-tag{font-size:8px;letter-spacing:1.2px;margin-top:5px}
.footer-claim{position:absolute;left:85px;top:94px;font-size:9px;font-weight:900}
.quick{position:absolute;left:345px;top:45px}
.quick h3,.about h3{font-size:11.5px;font-weight:900}
.quick ul{list-style:none;margin-top:30px}
.quick li{font-size:9.5px;font-weight:900;line-height:18.6px}
.about{position:absolute;left:483px;top:45px;width:210px}
.about h3{font-size:10px}
.about .rule{width:26px;height:1px;background:#7c8499;margin-top:10px}
.about p{font-size:9.6px;font-weight:900;line-height:12.4px;margin-top:24px}
.social{display:flex;gap:5px;margin-top:22px}
.social span{width:21px;height:21px;border-radius:50%;background:var(--navy-2);border:1px solid #2c3550}
</style>
</head>
<body>

<header class="site-header">
  <div class="brand">
    <div class="brand-name"><span class="brand-mark"></span>SURGE</div>
    <div class="brand-tag">MARKETING VIDEOS MADE FOR YOU</div>
  </div>
  <nav class="main-nav">
    <span>Home</span><span>How It Works</span><span>Examples</span><span>FAQ</span><span>Contact Us</span><span class="active">Pricing</span><span>Calendar</span>
  </nav>
  <span class="login">Log In</span>
  <span class="signup">Sign Up</span>
</header>

<h1 class="page-title">NO HIDDEN CHARGES! CHOOSE YOUR DEAL!</h1>

<section class="pricing">
  <div class="col">
    <div class="col-head features-head">FEATURES</div>
    <div class="cells">
      <div class="cell">VIDEOS INCLUDED</div><div class="cell">COST PER VIDEO FORMAT</div><div class="cell">DELIVERY SPEED</div><div class="cell">REVISIONS</div><div class="cell">FINAL FILE FORMATS</div><div class="cell">WIDE SCREEN VIDEO FORMAT</div><div class="cell">LARGE SQUARE VIDEO FORMAT</div><div class="cell">VERTICAL VIDEO FORMAT</div><div class="cell">PAGE COVER VIDEO FORMAT</div><div class="cell">HOLIDAY THEME VIDEO</div><div class="cell">SEASONAL THEME VIDEO</div><div class="cell">CONTENT DONE FOR YOU</div><div class="cell">FULL BRANDING IN VIDEO</div><div class="cell">FULL COPYRIGHT OWNERSHIP</div><div class="cell">FULL RESELLING RIGHTS</div><div class="cell">PREMIUM VIDEO CLIPS</div><div class="cell">USE MY IMAGES</div><div class="cell">USE MY VIDEO FOOTAGE</div><div class="cell">USE MY BACKGROUND MUSIC</div><div class="cell">FULLY LICENSED<br>BACKGROUND MUSIC</div>
    </div>
  </div>

  <div class="col">
    <div class="col-head">
      <div class="plan-name"><h2>AL A CARTE</h2><p>AS NEEDED BASIS</p></div>
      <div class="plan-price">STARTS AT ONLY<strong>$37.00</strong>VIDEO FORMAT</div>
    </div>
    <div class="cells">
      <div class="cell">CUSTOM</div><div class="cell">Starts @ $37/video</div><div class="cell">24 HOURS</div><div class="cell">UNLIMITED</div><div class="cell">Mp4 FULL HD 1080P</div><div class="cell">INCLUDED</div><div class="cell">INCLUDED</div><div class="cell">INCLUDED</div><div class="cell">INCLUDED</div><div class="cell">OPTIONAL</div><div class="cell">OPTIONAL</div><div class="cell">INCLUDED</div><div class="cell">INCLUDED</div><div class="cell">INCLUDED</div><div class="cell">INCLUDED</div><div class="cell">INCLUDED</div><div class="cell">INCLUDED</div><div class="cell">INCLUDED</div><div class="cell">INCLUDED</div><div class="cell">INCLUDED</div>
      <div class="qty"><span>-</span><span>1</span><span>+</span></div>
      <div class="sum"><span>Total</span><span>$149</span></div>
      <div class="sum"><span>Discount</span><span>$29.80</span></div>
      <div class="sum"><span>Price Per Video</span><span>$119.20</span></div>
      <div class="sum grand"><span>Grand Total</span><span>$119.20</span></div>
      <span class="buy low">BUY NOW</span>
    </div>
  </div>

  <div class="col popular">
    <div class="col-head">
      <div class="plan-name"><h2>SUBSCRIPTION</h2><p>NEW VIDEO ADS<br>MONTHLY</p></div>
      <div class="plan-price">STARTS AT ONLY<strong>$16.00</strong>VIDEO FORMAT</div>
    </div>
    <div class="cells">
      <div class="cell">CUSTOM</div><div class="cell">Starts @ $16/video</div><div class="cell">24 HOURS</div><div class="cell">UNLIMITED</div><div class="cell">Mp4 FULL HD 1080P</div><div class="cell">INCLUDED</div><div class="cell">INCLUDED</div><div class="cell">INCLUDED</div><div class="cell">INCLUDED</div><div class="cell">INCLUDED</div><div class="cell">INCLUDED</div><div class="cell">INCLUDED</div><div class="cell">INCLUDED</div><div class="cell">INCLUDED</div><div class="cell">INCLUDED</div><div class="cell">INCLUDED</div><div class="cell">INCLUDED</div><div class="cell">INCLUDED</div><div class="cell">INCLUDED</div><div class="cell">INCLUDED</div>
      <div class="qty"><span>-</span><span>1</span><span>+</span></div>
      <div class="sum"><span>Total</span><span>$99</span></div>
      <div class="sum"><span>Discount</span><span>$19.80</span></div>
      <div class="sum"><span>Price Per Video</span><span>$79.20</span></div>
      <div class="sum grand"><span>Grand Total</span><span>$79.20</span></div>
      <span class="buy low">BUY NOW</span>
    </div>
  </div>

  <div class="col">
    <div class="col-head">
      <div class="plan-name"><h2>HOLIDAY PKG</h2><p>17 HOLIDAY THEMED<br>VIDEOS</p></div>
      <div class="plan-price">ONLY<strong>$14.00</strong>VIDEO FORMAT</div>
    </div>
    <div class="cells">
      <div class="cell">17</div><div class="cell">$14/video</div><div class="cell">3-5 DAYS</div><div class="cell">UNLIMITED</div><div class="cell">Mp4 FULL HD 1080P</div><div class="cell">INCLUDED</div><div class="cell">INCLUDED</div><div class="cell">INCLUDED</div><div class="cell">INCLUDED</div><div class="cell">INCLUDED</div><div class="cell">NOT INCLUDED</div><div class="cell">INCLUDED</div><div class="cell">INCLUDED</div><div class="cell">INCLUDED</div><div class="cell">INCLUDED</div><div class="cell">INCLUDED</div><div class="cell">INCLUDED</div><div class="cell">INCLUDED</div><div class="cell">INCLUDED</div><div class="cell">INCLUDED</div>
      <span class="buy">BUY NOW</span>
    </div>
  </div>

  <div class="col">
    <div class="col-head">
      <div class="plan-name"><h2>SEASON PKG</h2><p>4 SEASONAL THEMED<br>VIDEOS</p></div>
      <div class="plan-price">ONLY<strong>$18.00</strong>VIDEO FORMAT</div>
    </div>
    <div class="cells">
      <div class="cell">4</div><div class="cell">$18/video</div><div class="cell">3-5 DAYS</div><div class="cell">UNLIMITED</div><div class="cell">Mp4 FULL HD 1080P</div><div class="cell">INCLUDED</div><div class="cell">INCLUDED</div><div class="cell">INCLUDED</div><div class="cell">INCLUDED</div><div class="cell">NOT INCLUDED</div><div class="cell">INCLUDED</div><div class="cell">INCLUDED</div><div class="cell">INCLUDED</div><div class="cell">INCLUDED</div><div class="cell">INCLUDED</div><div class="cell">INCLUDED</div><div class="cell">INCLUDED</div><div class="cell">INCLUDED</div><div class="cell">INCLUDED</div><div class="cell">INCLUDED</div>
      <span class="buy">BUY NOW</span>
    </div>
  </div>

  <div class="col">
    <div class="col-head">
      <div class="plan-name"><h2>SOCIAL MEDIA</h2><p>DAILY VIDEOS FOR YOUR<br>SOCIAL MEDIA</p></div>
      <div class="plan-price">ONLY<strong>$10.00</strong>VIDEO FORMAT</div>
    </div>
    <div class="cells">
      <div class="cell">30</div><div class="cell">$10/video</div><div class="cell">PRIOR TO NEXT MONTH</div><div class="cell">UNLIMITED</div><div class="cell">Mp4 FULL HD 1080P</div><div class="cell">NOT INCLUDED</div><div class="cell">INCLUDED</div><div class="cell">NOT INCLUDED</div><div class="cell">NOT INCLUDED</div><div class="cell">NOT INCLUDED</div><div class="cell">INCLUDED</div><div class="cell">INCLUDED</div><div class="cell">INCLUDED</div><div class="cell">INCLUDED</div><div class="cell">INCLUDED</div><div class="cell">INCLUDED</div><div class="cell">INCLUDED</div><div class="cell">INCLUDED</div><div class="cell">INCLUDED</div><div class="cell">INCLUDED</div>
      <span class="buy">BUY NOW</span>
    </div>
  </div>
</section>

<footer class="site-footer">
  <div class="footer-brand">
    <div class="brand-name"><span class="brand-mark"></span>SURGE</div>
    <div class="brand-tag">MARKETING VIDEOS MADE FOR YOU</div>
  </div>
  <p class="footer-claim">CREATED BY A MARKETER FOR MARKETERS.</p>
  <div class="quick">
    <h3>Quick Links</h3>
    <ul><li>How It Works</li><li>Term Of Service</li><li>Privacy Policy</li><li>Cookies Policy</li></ul>
  </div>
  <div class="about">
    <h3>About Us</h3>
    <div class="rule"></div>
    <p>With Surge, you simply let us know what you want to promote and we will have your video ad finished as soon as 24 hours!</p>
    <div class="social" aria-label="Social links"><span></span><span></span><span></span><span></span><span></span></div>
  </div>
</footer>

</body>
</html>
```